AUSTRALIA SUPPLEMENT - Protein label design - CREATIVE, FEMININE, UNIQUE

I need help with the design of what will be my line of supplements. (Protein, plant base, collagen , BCAAs, etc)
I'm starting off with protein isolate - with the flavours VANILLA, CHOCOLATE, BOYSENBERRY, HONEYCOMB.
I need help with the design of what the product will look like for my range.
(Great opportunity for further work)

Looking for a unique, elegant, stand out, feminine design, some slight sparkle or something that stands out on a shelf.
With symbols to represent what's in it, raised text. with some quirky cute things on it. (not sure what) Something that captured young womens eyes and easy to understand. things on it that appeals to women such as
LOW CALORIE, GREAT TASTING, GLUTEN FREE, 100 NATURAL, NATURALLY SWEETENED, HIGH PROTEIN.etc and whatever you can think of (open to ideas) but within PCF guidelines.

Mostly just after the look and creativity of what the front will look like. Don't have to worry about the back area.

My market will be for females aged 18-35

I have a activewear line called BRONTUK which will go with this. which I will attach the logo below amongst some other things that match my packaging. (again open to ideas)

I have attached a label of what one will look like( EXAMPLE).
. Among others that look nice But again I want to be different, unique to stand out. I don't want it to look like these. it's just the only ones I found online I liked that suit my market.

Feel free to ask any questions! :)
Updates

Extending time as I want this to be to be what will be on the shelves of many stores. I know that needs time to be able to do a quality job.

Target Market(s)

18-35

Industry/Entity Type

Supplement

Font styles to use
Serif
Script

Colors
f9d9e8
ffffff
fbd3d4
ecf7fb
e4daeb
cfeae6
eea4c8
fdfad7
f59195

Requirements
Must have
• Word - BRONTUK
PROTEIN ISOLATE
FLAVOUR
SYMBOLS

Looking for a unique, elegant, stand out, colour, feminine design, some slight sparkle or something that stands out on a shelf.

IT WILL BE ON A WHITE TUB or CLEAR - Perhaps detail on the lid
Nice to have
• Looking for a unique, elegant, stand out, colour, feminine design, some slight sparkle or something that stands out on a shelf. Something artsy.

will be on a white or clear tub with a white label background (possibly)
Should not have
• I don’t want it dark looking.
Something bright, vibrant, whites, pinks, sparkles (maybe) colours.

I don't want the word activewear on it.

```html
<!DOCTYPE html>
<html lang="en">
<head>
<meta charset="utf-8">
<title>BRONTUK Protein Isolate – Chocolate Label</title>
<link rel="stylesheet" href="https://fonts.googleapis.com/css2?family=Marcellus&family=Lato:wght@400;700&display=swap">
<style>
  :root{
    --page:#ffffff;
    --band-edge:#e8cbbf;
    --band-mid:#f3e3dc;
    --band-centre:#fbf5f3;
    --ink:#231f20;
    --cocoa:#3a2b29;
    --rose-gold:#d7b2a3;
    --rose-soft:#ecd3c9;
    --rose-line:#c9a191;
    --leaf:#e2c3b6;
    --choc:#4a3430;
  }
  *{margin:0;padding:0;box-sizing:border-box}
  html,body{width:1200px;height:1000px;overflow:hidden;background:var(--page)}
  .canvas{position:relative;width:1200px;height:1000px}
  .label{
    position:absolute;left:86px;top:347px;width:1028px;height:342px;
    background:radial-gradient(ellipse 400px 240px at 514px 170px,var(--band-centre) 0%,var(--band-mid) 55%,var(--band-edge) 100%);
    font-family:"Lato",sans-serif;color:var(--ink);
  }
  .brand{
    position:absolute;left:405px;top:40px;width:260px;text-align:center;white-space:nowrap;
    font-family:"Marcellus",serif;font-size:28px;line-height:1;letter-spacing:3px;color:var(--ink);
  }
  .brand-dot{display:inline-block;width:10px;height:10px;border-radius:50%;background:var(--ink);margin-right:8px;vertical-align:middle}
  .wreath{position:absolute;border-radius:50%;
    background:radial-gradient(circle,var(--leaf) 0%,rgba(226,195,182,0) 70%);}
  .wreath-upper{left:361px;top:55px;width:87px;height:96px}
  .wreath-lower-left{left:361px;top:193px;width:87px;height:66px}
  .wreath-lower-right{left:580px;top:193px;width:87px;height:66px}
  .product-name{
    position:absolute;left:0;width:100%;top:136px;text-align:center;
    font-family:"Marcellus",serif;font-weight:400;font-size:51px;line-height:1;color:var(--ink);letter-spacing:-0.5px;
  }
  .flavour{
    position:absolute;left:433px;top:196px;width:163px;height:24px;border-radius:12px;
    background:var(--cocoa);color:#fff;text-align:center;
    font-family:"Marcellus",serif;font-size:16px;line-height:24px;letter-spacing:3px;
  }
  .flavour-art{
    position:absolute;left:460px;top:232px;width:108px;height:54px;border-radius:6px;
    background:linear-gradient(160deg,#6a4b45,var(--choc) 60%,#2e201e);
  }
  .info{position:absolute;left:0;width:100%;text-align:center;font-weight:700;font-size:11px;line-height:14px;color:var(--ink)}
  .info-type{top:296px}
  .info-size{top:313px}
  .seal-ribbon{position:absolute;left:0;top:0;width:1028px;height:342px;pointer-events:none}
  .seal-text{font-family:"Marcellus",serif;fill:var(--ink);text-anchor:middle}
  .seal-small{font-family:"Lato",sans-serif;fill:var(--ink);text-anchor:middle}
  .macro-value{font-family:"Marcellus",serif;fill:var(--rose-line);text-anchor:middle}
  .macro-name{font-family:"Lato",sans-serif;fill:var(--rose-line);text-anchor:middle;letter-spacing:.5px}
</style>
</head>
<body>
<div class="canvas">
  <section class="label">
    <div class="wreath wreath-upper" role="img" aria-label="Rose-gold leafy branch curving around the brand name"></div>
    <div class="wreath wreath-lower-left" role="img" aria-label="Rose-gold leafy sprig, left"></div>
    <div class="wreath wreath-lower-right" role="img" aria-label="Rose-gold leafy sprig, right"></div>

    <div class="brand"><span class="brand-dot"></span>BRONTUK</div>

    <h1 class="product-name">PROTEIN ISOLATE</h1>
    <div class="flavour">CHOCOLATE</div>
    <div class="flavour-art" role="img" aria-label="Two squares of dark chocolate"></div>

    <p class="info info-type">Formulated Supplementary Food</p>
    <p class="info info-size">30 Serves / NT WT. 4lb (900g)</p>

    <svg class="seal-ribbon" viewBox="0 0 1028 342">
      <path d="M660 0 H713 V122 L686.5 109 L660 122 Z" fill="var(--rose-gold)"/>
      <circle cx="686" cy="59" r="40" fill="var(--rose-soft)" stroke="var(--rose-gold)" stroke-width="4" stroke-dasharray="3 2"/>
      <circle cx="686" cy="59" r="34" fill="none" stroke="var(--rose-line)" stroke-width="0.6"/>
      <text class="seal-text" x="686" y="45" font-size="9">100%</text>
      <text class="seal-text" x="686" y="58" font-size="10.5">NATURAL</text>
      <line x1="663" y1="63" x2="709" y2="63" stroke="var(--ink)" stroke-width="0.6" stroke-dasharray="1 1.5"/>
      <text class="seal-small" x="686" y="71" font-size="4.8">Naturally Sweetened</text>
      <text class="seal-small" x="686" y="78" font-size="4.8">Low Calorie</text>
      <text class="seal-small" x="686" y="85" font-size="4.8">Gluten Free</text>

      <g fill="none" stroke="var(--rose-line)" stroke-width="1">
        <circle cx="686" cy="234" r="17"/>
        <circle cx="686" cy="273" r="17"/>
        <circle cx="686" cy="312" r="17"/>
      </g>
      <text class="macro-value" x="686" y="234" font-size="9.5">23g</text>
      <text class="macro-name" x="686" y="242" font-size="5.5">PROTEIN</text>
      <text class="macro-value" x="686" y="273" font-size="9.5">2.1g</text>
      <text class="macro-name" x="686" y="281" font-size="5.5">CARBS</text>
      <text class="macro-value" x="686" y="312" font-size="9.5">2.1g</text>
      <text class="macro-name" x="686" y="320" font-size="5.5">FAT</text>
    </svg>
  </section>
</div>
</body>
</html>
```